Company brochure for Cedarline Stride Works, Inc.

We need a company brochure that lets referral sources know who we are, where are locations are and what services we offer. Our website is www.cedarlinestrideinc.com and we are on Facebook and Instagram. We need the brochure to feature both braces and prosthetics.

```html
<!DOCTYPE html>
<html lang="en">
<head>
<meta charset="utf-8">
<title>Cedarline Stride Works, Inc. — Trifold Brochure</title>
<link rel="stylesheet" href="https://fonts.googleapis.com/css2?family=Montserrat:wght@400;500;600;700;800;900&family=Oswald:wght@500;600&display=swap">
<style>
  :root {
    --blue: #1f4f9c;
    --blue-deep: #183f82;
    --navy-text: #1c3a78;
    --orange: #e2561b;
    --paper: #f0f1f4;
    --ink: #3a3f4a;
    --stage: #d6d6d6;
    --white: #ffffff;
  }
  * { box-sizing: border-box; margin: 0; padding: 0; }
  html, body { width: 1200px; height: 900px; overflow: hidden; }
  body {
    background: var(--stage);
    font-family: "Montserrat", Arial, sans-serif;
    color: var(--ink);
    position: relative;
  }
  .spread {
    position: absolute;
    width: 585px;
    height: 452px;
    background: var(--paper);
    box-shadow: 0 6px 18px rgba(0,0,0,.18);
    overflow: hidden;
  }
  .spread--outside { left: 8px; top: 224px; }
  .spread--inside { left: 607px; top: 224px; }
  .spread__art { position: absolute; inset: 0; }
  .block { position: absolute; }
  .body-copy { font-size: 4.8px; line-height: 1.45; color: var(--ink); }
  .body-copy + .body-copy { margin-top: 4px; }
  .on-blue .body-copy { color: rgba(255,255,255,.82); }

  /* outside spread */
  .welcome__kicker { font-size: 17px; font-weight: 900; color: var(--orange); line-height: 1; }
  .welcome__name { font-size: 11px; font-weight: 800; color: var(--navy-text); line-height: 1.2; margin: 3px 0 12px; }
  .checklist { list-style: none; margin: 7px 0 0 6px; }
  .checklist li { font-size: 4.6px; line-height: 1.9; color: var(--ink); }
  .checklist li::before { content: "\2713"; margin-right: 3px; color: var(--ink); }
  .subhead { font-size: 10px; font-weight: 500; color: var(--navy-text); line-height: 1.2; margin-bottom: 6px; }

  .contact { text-align: center; width: 165px; }
  .contact__kicker { font-size: 7px; font-weight: 700; color: var(--orange); }
  .contact__title { font-size: 19px; font-weight: 800; color: var(--navy-text); line-height: 1.05; }
  .contact__rule { width: 24px; height: 2px; background: var(--orange); margin: 6px auto 10px; }
  .contact__item { margin-bottom: 9px; }
  .contact__icon { display: block; margin: 0 auto 3px; }
  .contact__text { font-size: 5.6px; color: var(--ink); line-height: 1.35; letter-spacing: .02em; }

  .cover__kicker { font-family: "Oswald", Arial, sans-serif; font-weight: 600; font-size: 20px; color: var(--white); line-height: 1; }
  .cover__name { font-family: "Oswald", Arial, sans-serif; font-weight: 500; font-size: 13px; color: var(--white); line-height: 1.2; margin-top: 3px; }
  .cover__tagline { font-size: 6.8px; color: var(--white); line-height: 1.3; margin-top: 4px; }
  .cover__rule { width: 88px; height: 2px; background: var(--white); margin-top: 6px; }
  .cover__web { font-size: 9px; font-weight: 500; color: var(--white); letter-spacing: .02em; }

  .brand-seal {
    position: absolute; border-radius: 50%;
    background: var(--white); border: 3px solid var(--blue);
    display: flex; align-items: center; justify-content: center; text-align: center;
  }
  .brand-seal__name { font-size: 6.4px; font-weight: 700; color: var(--navy-text); line-height: 1.25; padding: 0 8px; }

  /* inside spread */
  .info__title { font-size: 14px; font-weight: 600; color: var(--white); line-height: 1.15; margin-bottom: 8px; }
  .info__subhead { font-size: 10px; font-weight: 500; color: var(--white); line-height: 1.2; margin: 12px 0 5px; }
  .info__note { font-size: 4.8px; line-height: 1.45; color: var(--white); font-weight: 600; margin-top: 4px; }

  .section-title { font-size: 10px; font-weight: 800; color: var(--navy-text); margin-bottom: 3px; }
  .section-title span, .headline span { color: var(--orange); }
  .services-title { font-size: 15px; font-weight: 800; color: var(--navy-text); margin: 10px 0 8px; }
  .service { display: flex; gap: 10px; align-items: flex-start; margin-bottom: 12px; }
  .service__icon { width: 24px; height: 22px; flex: none; border-radius: 3px; }
  .service__name { font-size: 7.4px; font-weight: 700; color: var(--ink); margin-bottom: 2px; }

  .headline { font-size: 13.5px; font-weight: 800; color: var(--navy-text); line-height: 1.05; margin-bottom: 6px; }
  .mission-title { font-size: 10px; font-weight: 800; color: var(--navy-text); margin: 12px 0 3px; }
</style>
</head>
<body>

<!-- Outside of the trifold: welcome flap, contact panel, front cover -->
<section class="spread spread--outside" aria-label="Brochure outside">
  <svg class="spread__art" width="585" height="452" viewBox="0 0 585 452" aria-hidden="true">
    <defs>
      <linearGradient id="peopleTone" x1="0" y1="0" x2="1" y2="1">
        <stop offset="0" stop-color="#c9d2dd"/>
        <stop offset=".5" stop-color="#e6e4e1"/>
        <stop offset="1" stop-color="#8fa3bd"/>
      </linearGradient>
      <linearGradient id="buildingTone" x1="0" y1="0" x2="0" y2="1">
        <stop offset="0" stop-color="#9ec3e6"/>
        <stop offset=".55" stop-color="#b4765e"/>
        <stop offset="1" stop-color="#8d8a86"/>
      </linearGradient>
      <linearGradient id="mapTone" x1="0" y1="0" x2="1" y2="1">
        <stop offset="0" stop-color="#eceff2"/>
        <stop offset="1" stop-color="#d7dde3"/>
      </linearGradient>
    </defs>
    <!-- top blue band across flap and contact panels -->
    <path d="M0,0 H390 V125 C330,92 250,62 170,56 C100,51 40,60 0,78 Z" fill="var(--blue)"/>
    <path d="M0,78 C40,60 100,51 170,56 C250,62 330,92 390,125" fill="none" stroke="var(--orange)" stroke-width="6"/>
    <!-- panel divider -->
    <rect x="195" y="0" width="195" height="452" fill="rgba(0,0,0,.025)"/>
    <!-- cover -->
    <rect x="390" y="0" width="195" height="452" fill="var(--blue)"/>
    <path d="M390,186 C450,176 520,172 585,178 V380 C520,385 450,405 390,438 Z" fill="url(#peopleTone)" role="img" aria-label="Photo of a clinician with two smiling older patients"/>
    <path d="M390,186 C450,176 520,172 585,178" fill="none" stroke="var(--orange)" stroke-width="6"/>
    <path d="M390,438 C450,405 520,385 585,380" fill="none" stroke="var(--orange)" stroke-width="5"/>
    <!-- building photo circle -->
    <circle cx="292" cy="70" r="41" fill="var(--white)" stroke="var(--orange)" stroke-width="2"/>
    <circle cx="292" cy="70" r="37" fill="url(#buildingTone)" role="img" aria-label="Photo of the clinic building"/>
    <!-- map -->
    <rect x="232" y="330" width="120" height="68" fill="url(#mapTone)" stroke="var(--orange)" stroke-width="1" role="img" aria-label="Street map showing the clinic location"/>
  </svg>

  <div class="block" style="left:16px; top:82px; width:166px;">
    <p class="welcome__kicker">Welcome to</p>
    <h1 class="welcome__name">Cedarline Stride Works, Inc.</h1>
    <p class="body-copy">Thank you for choosing Cedarline Stride for your orthotic and prosthetic needs. We pride ourselves on giving each patient high quality care and service under the direction of your physician. Our qualified and friendly staff is ready to help with all your questions.</p>
    <p class="body-copy">To help you prepare for your first visit we have created a Patient Information page to explain the process and prepare you for your first visit.</p>
    <ul class="checklist">
      <li>Patient Information Form</li>
      <li>Assignment of Benefits</li>
      <li>PCP-Patient Contact Preference/Medicare History</li>
      <li>Medicare Supplier Standards</li>
      <li>Medical Release</li>
      <li>Summary of Notice of Privacy Practices</li>
    </ul>
    <h2 class="subhead" style="margin-top:14px;">What to expect at your first appointment.</h2>
    <p class="body-copy">When you call one of our 7 convenient offices our friendly staff will ask about your situation so we can judge how much time your appointment will need. We will ask for your insurance details, your diagnosis, your referring physician and what item is prescribed. We will then book a time at a location that is convenient for you.</p>
    <p class="body-copy">Plan on arriving 10-15 minutes early to fill out any forms that are needed.</p>
  </div>

  <div class="block contact" style="left:210px; top:146px;">
    <p class="contact__kicker">Get in touch</p>
    <h2 class="contact__title">Contact</h2>
    <div class="contact__rule"></div>
    <div class="contact__item">
      <svg class="contact__icon" width="9" height="9" viewBox="0 0 10 10" aria-hidden="true"><circle cx="5" cy="5" r="5" fill="var(--blue)"/><circle cx="5" cy="5" r="2.6" fill="none" stroke="#fff" stroke-width=".8"/><path d="M2.4,5 H7.6 M5,2.4 V7.6" stroke="#fff" stroke-width=".6"/></svg>
      <p class="contact__text">WWW.CEDARLINESTRIDEINC.COM</p>
    </div>
    <div class="contact__item">
      <svg class="contact__icon" width="9" height="9" viewBox="0 0 10 10" aria-hidden="true"><circle cx="5" cy="5" r="5" fill="var(--blue)"/><path d="M3.3,3 C3.3,5.5 4.6,6.8 7,6.9 L7.2,6 L6.2,5.5 L5.7,6 C4.9,5.6 4.4,5.1 4,4.3 L4.5,3.8 L4,2.8 Z" fill="#fff"/></svg>
      <p class="contact__text">(555) 014-2290</p>
    </div>
    <div class="contact__item">
      <svg class="contact__icon" width="9" height="9" viewBox="0 0 10 10" aria-hidden="true"><circle cx="5" cy="5" r="5" fill="var(--blue)"/><path d="M5,2.3 C6.3,2.3 7,3.2 7,4.2 C7,5.4 5,7.6 5,7.6 C5,7.6 3,5.4 3,4.2 C3,3.2 3.7,2.3 5,2.3 Z" fill="#fff"/><circle cx="5" cy="4.2" r=".8" fill="var(--blue)"/></svg>
      <p class="contact__text">210 BIRCHWOOD LANE<br>FAIRMONT HILLS, MO 63000</p>
    </div>
  </div>

  <div class="block" style="left:408px; top:30px; width:170px;">
    <p class="cover__kicker">Welcome to</p>
    <p class="cover__name">Cedarline Stride Works</p>
    <p class="cover__tagline">Where we create custom made<br>solutions that work for you!</p>
    <div class="cover__rule"></div>
  </div>
  <div class="brand-seal" style="left:447px; top:122px; width:80px; height:80px;">
    <p class="brand-seal__name">Cedarline Stride Works, Inc.</p>
  </div>
  <p class="block cover__web" style="left:418px; top:418px;">www.cedarlinestrideinc.com</p>
</section>

<!-- Inside of the trifold: visit info, about & services, mission -->
<section class="spread spread--inside" aria-label="Brochure inside">
  <svg class="spread__art" width="585" height="452" viewBox="0 0 585 452" aria-hidden="true">
    <defs>
      <linearGradient id="walkerTone" x1="0" y1="0" x2="1" y2="1">
        <stop offset="0" stop-color="#6f7a5a"/>
        <stop offset=".5" stop-color="#6b5a48"/>
        <stop offset="1" stop-color="#3d3b36"/>
      </linearGradient>
      <linearGradient id="babyTone" x1="0" y1="0" x2="1" y2="1">
        <stop offset="0" stop-color="#7e9a6a"/>
        <stop offset="1" stop-color="#e8d9cd"/>
      </linearGradient>
      <linearGradient id="wallTone" x1="0" y1="0" x2="1" y2="0">
        <stop offset="0" stop-color="#e7e3df"/>
        <stop offset="1" stop-color="#cfc9c3"/>
      </linearGradient>
      <linearGradient id="fittingTone" x1="0" y1="0" x2="1" y2="1">
        <stop offset="0" stop-color="#e08a3c"/>
        <stop offset="1" stop-color="#7a4a3a"/>
      </linearGradient>
    </defs>
    <rect x="0" y="0" width="195" height="452" fill="var(--blue)"/>
    <!-- panel 2 bottom photo strip -->
    <path d="M195,385 C240,372 300,360 390,340 V452 H195 Z" fill="url(#wallTone)" role="img" aria-label="Photo of braces and orthotic devices displayed on a clinic wall"/>
    <path d="M195,385 C240,372 300,360 390,340" fill="none" stroke="var(--orange)" stroke-width="5"/>
    <!-- panel 3 large photo -->
    <path d="M390,300 C450,250 520,236 585,236 V452 H390 Z" fill="url(#walkerTone)" role="img" aria-label="Photo of a man walking outdoors on a prosthetic leg"/>
    <path d="M390,300 C450,250 520,236 585,236" fill="none" stroke="var(--orange)" stroke-width="7"/>
    <!-- circle photos -->
    <circle cx="438" cy="314" r="41" fill="var(--white)"/>
    <circle cx="438" cy="314" r="38" fill="url(#babyTone)" stroke="var(--blue)" stroke-width="3" role="img" aria-label="Photo of a smiling baby wearing a cranial helmet"/>
    <circle cx="355" cy="386" r="36" fill="var(--white)"/>
    <circle cx="355" cy="386" r="33" fill="url(#fittingTone)" stroke="var(--blue)" stroke-width="3" role="img" aria-label="Photo of a clinician fitting a brace on a child"/>
  </svg>

  <div class="block on-blue" style="left:12px; top:26px; width:172px;">
    <h2 class="info__title">What information should you bring?</h2>
    <p class="body-copy">You should bring the forms you filled out from this website along with your insurance card and the prescription your physician gave you. Bring any X-rays if asked when booking. If you already have an orthotic or prosthetic device, bring it with you even if worn out, broken or outgrown. If it goes in a shoe, bring the shoes you plan to wear most often with it. A family member or friend is welcome to come along; they can help with instructions and questions you may not think to ask.</p>
    <h3 class="info__subhead">What to expect during your appointment.</h3>
    <p class="body-copy">After filling out the paperwork our staff will weigh you and take your height, as this is needed to show growth or weight change for insurance coverage. You will then be shown to an exam room and one of our practitioners will do a full evaluation. They will discuss your options based on your needs and your coverage. You will be measured or cast depending on your needs.</p>
    <h3 class="info__subhead">Insurance Benefits</h3>
    <p class="body-copy">Our charges are not subject to an office visit co-pay; we bill under your policy's DME or orthotic benefits. Our front desk will verify your benefits and explain the quote to you, including any estimated co-insurance. Most policies require the insured to pay a share of the total after their contracted discount and annual deductible. You will pay half of your co-insurance to start work on your device and the balance when you are fit.</p>
    <p class="info__note">*We urge you to be proactive and contact your insurance carrier before your visit to verify your coverage for orthotics and prosthetics, including any deductible. If you need help with codes or procedures our staff will be happy to assist you.</p>
  </div>

  <div class="block" style="left:206px; top:24px; width:174px;">
    <h2 class="section-title">About <span>Us</span></h2>
    <p class="body-copy">Cedarline Stride Works has provided quality, compassionate care to residents of St. Louis and Southern Illinois since 1983. A recognized leader in the field, our experts work as a team to create the most functional orthotic, prosthetic and pedorthic solutions using the latest technology. Our patient-centered team works closely with your doctor, nurse, therapist and family to create custom made solutions that work for you.</p>
    <p class="body-copy">Our practitioners make up the largest and most experienced O &amp; P practice in the area. We have both adult and pediatric specialists, and our certified practitioners attend ongoing education programs and clinics so our patients get the latest developments. Our central fabrication facility lets us build your device with speed, quality and convenience.</p>
    <h2 class="services-title">Services <span style="color:var(--orange)">Us</span></h2>
    <div class="service">
      <div class="service__icon" style="background:linear-gradient(135deg,#f08a3a,#d83a2a);" role="img" aria-label="Insurance folder icon"></div>
      <div><p class="service__name">Insurance Contracts</p><p class="body-copy">We are contracted with almost all local insurance plans and offer full insurance billing for our patients.</p></div>
    </div>
    <div class="service">
      <div class="service__icon" style="background:linear-gradient(135deg,#4c7fc8,#c9d6e8);" role="img" aria-label="Clock and map icon"></div>
      <div><p class="service__name">Locations &amp; Hours</p><p class="body-copy">With 7 offices in the metropolitan area we have a location near you.</p></div>
    </div>
    <div class="service">
      <div class="service__icon" style="background:linear-gradient(135deg,#2b4f9c,#e9edf3);" role="img" aria-label="Orthotic and prosthetic devices icon"></div>
      <div><p class="service__name">Our Products</p><p class="body-copy">We offer the very best in orthotic, prosthetic and pedorthic devices.</p></div>
    </div>
  </div>
  <div class="brand-seal" style="left:244px; top:352px; width:68px; height:68px;">
    <p class="brand-seal__name" style="font-size:5.6px;">Cedarline Stride Works, Inc.</p>
  </div>

  <div class="block" style="left:402px; top:24px; width:172px;">
    <h2 class="headline">MOVE NATURALLY<br><span>SAFETY</span></h2>
    <p class="body-copy">With powered toe lift and stumble recovery to help reduce the risk of trips and falls.</p>
    <p class="body-copy">After 32 years of trips and falls as an amputee, Dale Morrow learned to avoid certain terrain like ramps, grass and mulch whenever possible. But things changed the day Dale switched to a StrideFlex Leg. Now he says, "I don't really think about the terrain I'm walking on. It's not an issue. I feel so safe walking on my StrideFlex Leg that I am more active than I have been in decades."</p>
    <h2 class="mission-title">Our <span style="color:var(--orange)">Mission</span></h2>
    <p class="body-copy">We are people committed to using every scientific and technical development available to restore the physical capabilities of the disabled. By combining know-how and modern technology we seek to help the "disabled" become "enabled".</p>
    <p class="body-copy">Our pledge is to use all of our orthotic and prosthetic resources to empower individuals with physical challenges to take part in all facets of life.</p>
  </div>
</section>

</body>
</html>
```